Stellan App | Pre-Launch Homepage

Dear designer,
Stellan is a soon to be launched innovative & free social platform for collaborative addictions quitting.
We require a design for our pre-launch homepage that will elevate our basic wireframes to the next level.
We would like the wireframes to serve as a guideline only, and not as a final version of the design. If you have cool ideas - we would appreciate your creativity!
* This is a pre-launch website for a mobile app, and as such the design must be consistent with the general style, design and atmosphere of the app (see screenshot in the shared Drive link).
* We liked the style and feel of the following website: http://plumvane.com/ - Please let's use it as a reference as well.
* The existing text in the wireframes is there just to represent a place for text. Copy will be edited by us after the design is done.
Please find the wireframes attached, and all relevant design assets and app screenshots in the following Drive shared link -
https://files.orbelink.com/open?id=7K204XqR3tPmHc8Lw2Jd61VnaGzT
Thanks,
Marcus
Industry/Entity Type
Social
Number of Pages Required
1 page
Look and feel
Each slider illustrates characteristics of the customer's brand and the style your logo design should communicate.

```html
<!DOCTYPE html>
<html lang="en">
<head>
<meta charset="utf-8">
<title>Stellan | Pre-Launch Homepage</title>
<link href="https://fonts.googleapis.com/css2?family=Oswald:wght@500;700&family=Open+Sans:wght@400;700&display=swap" rel="stylesheet">
<style>
:root{
  --orange:#f08a1c;
  --orange-deep:#e2701a;
  --green:#5a9a1e;
  --ink:#3a3a3a;
  --muted:#777;
  --white:#fff;
  --paper:#f1ede3;
  --line:#dcdcdc;
  --night:#1e1d22;
  --phone:#151515;
}
*{box-sizing:border-box;margin:0;padding:0}
html,body{width:1200px;height:4644px;overflow:hidden}
body{font-family:"Open Sans",Arial,sans-serif;color:var(--ink);background:var(--white);position:relative}
section,footer{position:absolute;left:0;width:1200px;overflow:hidden}
.abs{position:absolute}
.heading{font-family:"Oswald",Impact,sans-serif;font-weight:700;color:var(--orange);font-size:48px;letter-spacing:1px}
.copy{font-size:17px;line-height:27px;color:var(--muted)}
.copy b{color:var(--ink)}

/* hero */
.hero{top:0;height:1192px;color:var(--white)}
.hero-backdrop{position:absolute;inset:0;background:
  radial-gradient(ellipse at 25% 55%,rgba(196,70,40,.55),transparent 45%),
  radial-gradient(ellipse at 80% 35%,rgba(210,120,40,.45),transparent 40%),
  radial-gradient(ellipse at 55% 80%,rgba(90,60,70,.6),transparent 50%),
  linear-gradient(180deg,#2a2226 0%,#3b2a2a 50%,#2a2230 100%)}
.contact-tab{position:absolute;right:0;top:0;width:252px;height:44px;background:var(--orange-deep);color:var(--white);font-size:17px;font-weight:700;text-align:center;line-height:40px;border-bottom-left-radius:6px}
.brand{left:0;width:1200px;top:36px;text-align:center;font-family:"Oswald",Impact,sans-serif;font-weight:700;font-size:64px;color:var(--orange)}
.tagline{left:0;width:1200px;top:230px;text-align:center;font-size:30px;line-height:38px;font-weight:400}
.signup{left:336px;width:528px;height:112px;top:360px;background:rgba(0,0,0,.45);border-radius:6px;padding:18px 40px}
.signup p{font-size:15px;font-weight:700;text-align:center;margin-bottom:12px}
.field{display:flex;height:40px;border-radius:4px;overflow:hidden;background:var(--white)}
.field span{flex:1;color:#aaa;font-size:14px;line-height:40px;padding-left:14px}
.field strong{width:130px;background:var(--green);color:var(--white);font-size:14px;line-height:40px;text-align:center}
.devices{left:508px;top:568px}
.feature{top:790px;width:300px;text-align:center}
.feature h3{font-size:20px;font-weight:700;margin-top:22px}
.feature p{font-size:15px;line-height:22px;color:rgba(255,255,255,.7);margin-top:8px}
.badge{width:140px;height:140px;border-radius:50%;background:rgba(40,40,48,.8);margin:0 auto;display:flex;align-items:center;justify-content:center}

/* phone */
.phone{background:var(--phone);border-radius:34px;border:3px solid #444}
.phone .screen{position:absolute;left:14px;right:14px;top:80px;bottom:80px;background:var(--white)}
.phone .button{position:absolute;left:50%;bottom:22px;width:44px;height:44px;margin-left:-22px;border-radius:50%;border:2px solid #444}
.phone .speaker{position:absolute;left:50%;top:38px;width:64px;height:8px;margin-left:-32px;border-radius:4px;background:#333}

.fun{top:1192px;height:668px;border-bottom:2px solid var(--line)}
.inspire{top:1860px;height:660px;border-bottom:2px solid var(--line)}
.achieve{top:2520px;height:680px}
.soon{top:3200px;height:1080px;background:var(--paper)}
.side-item{width:230px;font-size:14px;line-height:21px;color:var(--muted)}
.side-item b{color:var(--ink)}

.signup.orange{background:var(--orange);top:4072px}
.signup.orange p{color:var(--white)}

.site-footer{top:4280px;height:364px;background:linear-gradient(180deg,#2b2a30,var(--night));color:var(--white);text-align:center}
.site-footer h4{font-size:20px;font-weight:700;margin-top:96px}
.socials{display:flex;justify-content:center;gap:14px;margin-top:24px}
.socials span{width:46px;height:46px;border-radius:50%;border:2px solid var(--white)}
.legal{font-size:13px;color:rgba(255,255,255,.7);margin-top:30px;line-height:44px}
</style>
</head>
<body>

<section class="hero">
  <div class="hero-backdrop" role="img" aria-label="Blurred warm-toned evening photo backdrop"></div>
  <div class="contact-tab">Contact Us</div>
  <div class="abs brand">Stellan</div>
  <h1 class="abs tagline">Stellan is a revolutionary &amp; free social platform<br>for collaborative addictions quitting.</h1>
  <div class="abs signup">
    <p>Subscribe below for the beta release and updates</p>
    <div class="field"><span>Enter your e-mail address</span><strong>Let me know!</strong></div>
  </div>
  <svg class="abs devices" width="184" height="64" viewBox="0 0 184 64" fill="none" stroke="#fff" stroke-width="4">
    <rect x="4" y="8" width="30" height="50" rx="4"/>
    <rect x="52" y="4" width="44" height="56" rx="4"/>
    <rect x="114" y="6" width="66" height="42" rx="3"/><path d="M147 48v10M132 60h30"/>
  </svg>
  <div class="abs feature" style="left:120px">
    <div class="badge"><svg width="80" height="80" viewBox="0 0 80 80"><circle cx="40" cy="40" r="30" fill="none" stroke="#e23b2e" stroke-width="18"/><circle cx="40" cy="40" r="30" fill="none" stroke="#fff" stroke-width="18" stroke-dasharray="23.5 23.5"/></svg></div>
    <h3>Never be Alone</h3><p>Forget what you know - Stellan makes it fun to quit.</p>
  </div>
  <div class="abs feature" style="left:450px">
    <div class="badge"><svg width="90" height="90" viewBox="0 0 90 90"><polygon points="45,6 56,34 86,35 62,54 71,84 45,66 19,84 28,54 4,35 34,34" fill="#f2c230"/></svg></div>
    <h3>Network Power</h3><p>Forget what you know - Stellan makes it fun to quit.</p>
  </div>
  <div class="abs feature" style="left:780px">
    <div class="badge"><div role="img" aria-label="Feathered headdress illustration" style="width:90px;height:90px;border-radius:50%;background:radial-gradient(circle,#e8e8e8,#9a9a9a)"></div></div>
    <h3>Stay Motivated</h3><p>Forget what you know - Stellan makes it fun to quit.</p>
  </div>
</section>

<section class="fun">
  <div class="abs phone" style="left:160px;top:66px;width:262px;height:560px">
    <div class="speaker"></div>
    <div class="screen"><div role="img" aria-label="Smiling clown illustration" style="position:absolute;left:50%;top:50%;width:150px;height:150px;margin:-75px;border-radius:50%;background:radial-gradient(circle,#ffd75a 40%,#f2a81e)"></div></div>
    <div class="button"></div>
  </div>
  <h2 class="abs heading" style="left:780px;top:200px">Fun</h2>
  <div class="abs copy" style="left:580px;top:278px;width:480px">
    <p>Forget what you know - <b>Stellan makes it fun to quit</b>. The battle between your good and bad demons comes to life in our <b>gamified approach</b> for managing your campaign.</p>
    <p style="margin-top:22px">Stellan gives you the opportunity to take an <b>active role</b> in helping your network to <b>smash</b> your common addictions as a team that's right we converted the cessation process into a social game.</p>
  </div>
</section>

<section class="inspire">
  <div class="abs phone" style="left:782px;top:70px;width:266px;height:560px">
    <div class="speaker"></div>
    <div class="screen"><div role="img" aria-label="Glowing light bulb illustration" style="position:absolute;left:50%;top:50%;width:140px;height:160px;margin:-80px -70px;border-radius:50% 50% 40% 40%;background:radial-gradient(circle,#ffd23a 45%,#f39a1a)"></div></div>
    <div class="button"></div>
  </div>
  <h2 class="abs heading" style="left:240px;top:220px">Inspire</h2>
  <div class="abs copy" style="left:180px;top:300px;width:470px">
    <p>One of the most important factors for successful quitting is the ability to <b>stay inspired</b> during the process.</p>
    <p style="margin-top:22px">That's why we designed Stellan as a platform where you can inspire and be inspired by a supportive network of awesome Stellan-ers!</p>
  </div>
</section>

<section class="achieve">
  <h2 class="abs heading" style="left:0;width:1200px;text-align:center;top:100px">Achieve</h2>
  <div class="abs copy" style="left:360px;width:480px;top:180px;text-align:center">
    <p>Stellan is built as a <b>pyramid of relationships</b> that makes use of the <b>Social Cognitive Theory</b>, to provide a powerful network of positive reinforcement.</p>
    <p style="margin-top:14px">The bigger you make it the stronger you get.</p>
  </div>
  <div class="abs phone" style="left:472px;top:340px;width:260px;height:400px">
    <div class="speaker"></div>
    <div class="screen" style="bottom:0"><div role="img" aria-label="Golden trophy with laurel illustration" style="position:absolute;left:50%;top:40px;width:150px;height:150px;margin-left:-75px;border-radius:50%;background:radial-gradient(circle,#ffd23a 40%,#f1a41c)"></div></div>
  </div>
  <svg class="abs" style="left:90px;top:400px" width="50" height="50" viewBox="0 0 50 50" fill="#aaa"><path d="M12 6h26v12a13 13 0 0 1-26 0z M22 31h6v8h8v5H14v-5h8z"/></svg>
  <div class="abs side-item" style="left:166px;top:400px">Stellan is built as a <b>pyramid of relationships</b> that makes use of the <b>Social Cognitive Theory</b>.</div>
  <svg class="abs" style="left:90px;top:520px" width="50" height="50" viewBox="0 0 50 50" fill="none" stroke="#aaa" stroke-width="4"><path d="M4 20h42l-6 24H10z M14 20l8-14M36 20l-8-14"/></svg>
  <div class="abs side-item" style="left:166px;top:520px">Stellan is built as a <b>pyramid of relationships</b> that makes use of the <b>Social Cognitive Theory</b>.</div>
  <svg class="abs" style="left:776px;top:400px" width="50" height="50" viewBox="0 0 50 50" fill="#aaa"><path d="M12 6h26v12a13 13 0 0 1-26 0z M22 31h6v8h8v5H14v-5h8z"/></svg>
  <div class="abs side-item" style="left:846px;top:400px">Stellan is built as a <b>pyramid of relationships</b> that makes use of the <b>Social Cognitive Theory</b>.</div>
  <svg class="abs" style="left:776px;top:520px" width="50" height="50" viewBox="0 0 50 50" fill="none" stroke="#aaa" stroke-width="4"><path d="M4 20h42l-6 24H10z M14 20l8-14M36 20l-8-14"/></svg>
  <div class="abs side-item" style="left:846px;top:520px">Stellan is built as a <b>pyramid of relationships</b> that makes use of the <b>Social Cognitive Theory</b>.</div>
</section>

<section class="soon">
  <h2 class="abs heading" style="left:0;width:1200px;text-align:center;top:88px">Coming Soon</h2>
  <div class="abs phone" style="left:472px;top:176px;width:258px;height:546px">
    <div class="speaker"></div>
    <div class="screen" role="img" aria-label="App screen showing a profile and quitting progress" style="background:linear-gradient(180deg,#3a3f36,#1f2420)"></div>
    <div class="button"></div>
  </div>
  <div class="abs" style="left:444px;top:760px;display:flex;gap:42px">
    <div style="width:76px;height:76px;border-radius:12px;background:#2d9cdb"></div>
    <div style="width:76px;height:76px;border-radius:50%;background:#b9b9b9"></div>
    <div style="width:76px;height:76px;background:#1e78d2"></div>
  </div>
</section>
<div class="abs signup orange">
  <p>Subscribe below for the beta release and updates</p>
  <div class="field"><span>Enter your e-mail address</span><strong>Let me know!</strong></div>
</div>

<footer class="site-footer">
  <h4>Join The Revolution</h4>
  <div class="socials"><span></span><span></span><span></span></div>
  <p class="legal">Copyright © 2015 Stellan Ltd.<br>Contact Us | T&amp;Cs | Privacy Policy</p>
</footer>

</body>
</html>
```